Business Card Design

Hunting Ranch in the Texas hill country (Deer, Turkey, Quail)

Want Marcus on one side and Sissy on the other.
We are looking for a Jack Rabbit NOT a cottontail bunny

Industry/Entity Type

Business

Contact Information for Business Card

Lone Sparrow Ranch
Junction Texas
Marcus Holloway Sissy Holloway
14 Pecan Hollow Ln. 14 Pecan Hollow Ln.
Cedar Bluff, Texas U.S.A. Cedar Bluff, Texas U.S.A.
281-472-5819 281-384-2957

```html
<!DOCTYPE html>
<html lang="en">
<head>
<meta charset="utf-8">
<title>Lone Sparrow Ranch — Business Cards</title>
<link rel="stylesheet" href="https://fonts.googleapis.com/css2?family=Ubuntu:wght@400;500&display=swap">
<style>
  :root {
    --backdrop: #ebe8e3;
    --card-top: #ffffff;
    --card-bottom: #ececec;
    --ink-brown: #5b3a2b;
    --accent-green: #a8c93a;
    --rule-grey: #cfcfcf;
  }
  * { margin: 0; padding: 0; box-sizing: border-box; }
  html, body {
    width: 1200px; height: 780px; overflow: hidden;
    background: var(--backdrop);
    font-family: "Ubuntu", sans-serif;
    color: var(--ink-brown);
  }
  .stage {
    width: 1200px; height: 780px;
    display: flex; align-items: center; justify-content: center; gap: 40px;
  }
  .card {
    position: relative;
    width: 520px; height: 300px;
    border-radius: 18px;
    background: linear-gradient(160deg, var(--card-top), var(--card-bottom));
    box-shadow: 0 2px 6px rgba(0,0,0,0.12);
    display: flex;
    overflow: hidden;
  }
  .brand-side {
    width: 260px; height: 100%;
    display: flex; flex-direction: column; align-items: center; justify-content: center;
    gap: 22px;
  }
  .brand-mark {
    width: 100px; height: 100px; border-radius: 50%;
    border: 9px solid var(--ink-brown);
  }
  .brand-name {
    font-size: 23px; font-weight: 400; letter-spacing: 0.2px;
    color: var(--ink-brown);
    white-space: nowrap;
  }
  .divider {
    width: 1px; margin: 34px 0;
    background: var(--rule-grey);
  }
  .contact-side {
    flex: 1; padding: 62px 0 0 30px;
  }
  .person-name {
    font-size: 25px; font-weight: 400; margin-bottom: 42px;
    white-space: nowrap;
  }
  .contact-line {
    font-size: 16px; line-height: 27px;
    display: flex; align-items: center; gap: 7px;
    white-space: nowrap;
  }
  .phone-icon { width: 15px; height: 15px; flex: none; }
</style>
</head>
<body>
<main class="stage">

  <article class="card card--sissy">
    <section class="brand-side">
      <div class="brand-mark"></div>
      <p class="brand-name">Lone Sparrow Ranch</p>
    </section>
    <div class="divider"></div>
    <section class="contact-side">
      <h2 class="person-name">Sissy Holloway</h2>
      <p class="contact-line">14 Pecan Hollow Ln.</p>
      <p class="contact-line">
        <svg class="phone-icon" viewBox="0 0 16 16" aria-hidden="true">
          <rect width="16" height="16" rx="3" fill="var(--accent-green)"/>
          <path d="M4.5 3.5h2l1 2.5-1.3 1a6 6 0 0 0 2.8 2.8l1-1.3 2.5 1v2c0 .6-.5 1-1 1A8.5 8.5 0 0 1 3.5 4.5c0-.5.4-1 1-1z" fill="#fff"/>
        </svg>
        281-384-2957
      </p>
      <p class="contact-line">Cedar Bluff, Texas U.S.A.</p>
    </section>
  </article>

  <article class="card card--marcus">
    <section class="brand-side">
      <div class="brand-mark"></div>
      <p class="brand-name">Lone Sparrow Ranch</p>
    </section>
    <div class="divider"></div>
    <section class="contact-side">
      <h2 class="person-name">Marcus Holloway</h2>
      <p class="contact-line">14 Pecan Hollow Ln.</p>
      <p class="contact-line">
        <svg class="phone-icon" viewBox="0 0 16 16" aria-hidden="true">
          <rect width="16" height="16" rx="3" fill="var(--accent-green)"/>
          <path d="M4.5 3.5h2l1 2.5-1.3 1a6 6 0 0 0 2.8 2.8l1-1.3 2.5 1v2c0 .6-.5 1-1 1A8.5 8.5 0 0 1 3.5 4.5c0-.5.4-1 1-1z" fill="#fff"/>
        </svg>
        281-472-5819
      </p>
      <p class="contact-line">Cedar Bluff, Texas U.S.A.</p>
    </section>
  </article>

</main>
</body>
</html>
```